Wordpress Design Project - MarbleQuay

I would like our existing old website at www.marblequay.example to be redesigned to a more modern attractive site using Wordpress, a total of 5 web pages. And also installed onto our new web hosting site. Please visit the existing website using Microsoft Internet explorer to see the content.
The new site must be compatible with all popular web browsers and mobile devices (if possible).
There should be a contact button available on each page with an associated form in case an interested person wants to contact us. This form must be spam proof not allowing automated crawlers from activating it.

There are only 5 pages web pages to this MarbleQuay project.

```html
<!DOCTYPE html>
<html lang="en">
<head>
<meta charset="utf-8">
<title>MarbleQuay</title>
<link href="https://fonts.googleapis.com/css2?family=Roboto:ital,wght@0,400;0,700;1,700&family=Noticia+Text:ital@1&family=Oswald:wght@400&display=swap" rel="stylesheet">
<style>
:root{
  --ink:#333;
  --dark:#333436;
  --blue:#0d4a94;
  --blue-deep:#0a3d80;
  --accent:#1773c6;
  --white:#fff;
  --grey:#e6e6e6;
  --rule:#bbb;
  --footer-text:#e9e9e9;
}
*{margin:0;padding:0;box-sizing:border-box}
html,body{width:1044px;height:1200px;overflow:hidden}
body{position:relative;font-family:Arial,"Roboto",sans-serif;color:var(--ink);background:var(--white)}
.abs{position:absolute}
.topline{left:0;top:0;width:1044px;height:6px;background:var(--dark)}
.header{left:0;top:6px;width:1044px;height:116px;background:linear-gradient(#fff,#ececec)}
.brand{left:88px;top:30px;display:flex;align-items:center;gap:12px}
.brand-dot{width:48px;height:48px;border-radius:50%;background:var(--blue)}
.brand-name{font:700 28px "Roboto",sans-serif;color:var(--blue)}
.contact-top{right:100px;top:42px;font:700 12px "Roboto",sans-serif;text-align:right;color:var(--ink)}
.contact-top b{color:var(--accent)}
.tollfree{right:100px;top:60px;display:flex;align-items:center;gap:8px;border-top:1px dotted #999;border-bottom:1px dotted #999;padding:2px 0 4px}
.tollfree .icon{width:26px;height:26px;background:var(--accent);border-radius:3px;display:flex;align-items:center;justify-content:center}
.tollfree .label{font:400 19px "Oswald",sans-serif;color:#222}
.tollfree .num{font:400 23px "Oswald",sans-serif;color:var(--accent)}
.nav{left:0;top:122px;width:1044px;height:36px;background:var(--dark);display:flex;align-items:center;padding-left:89px;gap:0}
.nav a{font:italic 700 12px "Roboto",sans-serif;color:var(--white);text-decoration:none;text-transform:uppercase;margin-right:61px}
.nav a.active{background:var(--white);color:var(--blue);padding:5px 11px;border-radius:3px;margin-right:48px}
.hero{left:0;top:158px;width:1044px;height:334px;background:radial-gradient(ellipse at 40% 40%,#1656a3,var(--blue-deep))}
.hero-title{left:89px;top:38px;font:italic 400 30px "Noticia Text",serif;color:var(--white)}
.hero-title span{background:var(--white);color:#222;padding:0 4px;border-radius:3px}
.hero-sub{left:91px;top:83px;font:700 13px "Roboto",sans-serif;color:var(--white);width:400px;padding-bottom:10px;border-bottom:1px solid #4f7fbd}
.hero-text{left:91px;top:124px;width:400px;font:400 11.5px/19px Arial,sans-serif;color:var(--white)}
.btn-read{left:91px;top:271px;width:136px;height:35px;background:linear-gradient(#444,#1d1d1d);border-radius:4px;display:flex;align-items:center;justify-content:center;gap:8px;font:italic 400 18px "Noticia Text",serif;color:var(--white)}
.photo-circle{border-radius:50%;border:8px solid #f4f4f4;box-shadow:0 8px 20px rgba(0,0,0,.35)}
.welcome-title{left:91px;top:522px;font:italic 700 23px "Roboto",sans-serif;color:var(--ink);width:494px;border-bottom:1px dotted #999;padding-bottom:4px}
.welcome-title span{color:var(--blue)}
.welcome-lead{left:91px;top:559px;width:545px;font:700 12px/18px Arial,sans-serif;color:#333}
.features-title{left:92px;top:607px;font:700 12.5px Arial,sans-serif;color:var(--blue)}
.features{left:92px;top:628px;list-style:none;font:400 11px Arial,sans-serif;color:#333}
.features li{height:21px;padding-left:14px;position:relative}
.features li::before{content:"➡";position:absolute;left:0;top:0;font-size:8px;color:#333}
.video{left:700px;top:543px;width:230px;height:196px;background:#ececec;border-radius:16px;box-shadow:0 4px 8px rgba(0,0,0,.15)}
.video-frame{position:absolute;left:10px;top:10px;width:210px;height:158px;border-radius:12px;background:linear-gradient(135deg,#f2e6dc,#d8c3b0 60%,#eaded3)}
.play{position:absolute;left:76px;top:50px;width:58px;height:58px;border-radius:50%;background:rgba(60,60,60,.75);border:3px solid #ddd}
.video-cap{position:absolute;left:20px;top:177px;font:400 10px "Roboto",sans-serif;color:#222;display:flex;align-items:center;gap:3px}
.video-cap i{width:7px;height:7px;border-radius:50%;background:#e0331b;display:inline-block}
.cards{left:100px;top:774px;width:835px;height:221px;display:flex;border-left:1px dotted #999;border-top:1px dotted #999;border-right:1px dotted #999}
.card{flex:1;position:relative;border-right:1px dotted #999;padding:8px 8px 0}
.card:last-child{border-right:0}
.card-photo{width:100%;height:104px;border:5px solid #f1f1f1;box-shadow:0 0 2px #ccc}
.card h3{margin:11px 0 0 6px;font:italic 700 16px "Roboto",sans-serif;color:#333}
.card h3 span{color:var(--accent)}
.card p{margin:8px 0 0 6px;font:400 10.5px/16px Arial,sans-serif;letter-spacing:.3px;color:#444;text-align:justify;width:170px}
.view{position:absolute;right:12px;bottom:6px;display:flex;align-items:center;gap:5px;font:400 10.5px "Roboto",sans-serif;color:#333}
.plus{width:20px;height:20px;border-radius:50%;background:var(--accent);color:var(--white);font:700 16px/20px Arial,sans-serif;text-align:center}
.footer{left:0;top:1051px;width:1044px;height:149px;background:var(--dark)}
.foot-brand{left:96px;top:40px;display:flex;align-items:center;gap:12px}
.foot-brand .brand-dot{background:#bbb;width:52px;height:52px}
.foot-brand .brand-name{color:#ccc;font-size:28px}
.vrule{top:16px;width:1px;height:120px;border-left:1px dotted #777}
.foot-links{left:396px;top:31px;font:400 11px Arial,sans-serif;color:var(--footer-text)}
.social{left:460px;top:64px;display:flex;gap:13px}
.social i{width:32px;height:32px;border-radius:50%;background:#2f6fb8;border:2px solid #ddd;display:block}
.copy{left:396px;top:116px;font:400 11px Arial,sans-serif;color:var(--footer-text)}
.foot-contact{right:99px;top:8px;text-align:right;color:var(--footer-text)}
.foot-contact h4{font:700 17px "Roboto",sans-serif;color:#bbb}
.foot-contact .fname{font:italic 700 18px "Roboto",sans-serif;margin-top:12px}
.foot-contact .addr{font:400 11px/17px Arial,sans-serif}
.foot-phone{right:99px;top:100px;display:flex;align-items:center;gap:10px;font:400 26px "Oswald",sans-serif;color:#ccc;letter-spacing:1px}
.foot-phone .ring{width:30px;height:30px;border-radius:50%;border:2px solid #ccc;display:flex;align-items:center;justify-content:center}
</style>
</head>
<body>
<div class="abs topline"></div>
<header class="abs header"></header>
<div class="abs brand"><span class="brand-dot"></span><span class="brand-name">MarbleQuay</span></div>
<div class="abs contact-top"><b>Info</b>@marblequay.example &nbsp;<b>Fax:</b> 555-010-2815</div>
<div class="abs tollfree">
  <span class="icon"><svg width="16" height="16" viewBox="0 0 24 24"><path fill="#fff" d="M6.6 10.8a15 15 0 0 0 6.6 6.6l2.2-2.2a1 1 0 0 1 1-.25 11.4 11.4 0 0 0 3.6.57 1 1 0 0 1 1 1V20a1 1 0 0 1-1 1A17 17 0 0 1 3 4a1 1 0 0 1 1-1h3.5a1 1 0 0 1 1 1c0 1.25.2 2.45.57 3.57a1 1 0 0 1-.25 1z"/></svg></span>
  <span class="label">CALL US TOLL-FREE ON</span><span class="num">1800 555 017</span>
</div>
<nav class="abs nav">
  <a class="active">Home</a><a>Telephone VoIP Solution</a><a>IP, LAN &amp; Internet</a><a>Support</a><a>Services</a><a>Contact Us</a>
</nav>

<section class="abs hero">
  <h1 class="abs hero-title">MarbleQuay <span>Provides</span> Complete</h1>
  <p class="abs hero-sub">Telephone Voip Pbx Solutions For Businesses Large And Small.</p>
  <p class="abs hero-text">Our team of telecom engineers will design and install the best business telephone VoIP PBX solution for your requirements. System features include: standard and advanced PBX call control actions, video telephone calling, toll free calling any where VoIP PBX solution for your requirements. System features include: standard and advanced VoIP PBX solution for your requirements. System features include: standard and advanced PBX call control actions.</p>
  <div class="abs btn-read">Read More
    <svg width="18" height="18" viewBox="0 0 18 18"><circle cx="9" cy="9" r="8" fill="#fff"/><path d="M5 9h7M9 5.5 12.5 9 9 12.5" stroke="#222" stroke-width="2" fill="none"/></svg>
  </div>
  <div class="abs photo-circle" style="left:710px;top:12px;width:134px;height:134px;background:linear-gradient(135deg,#eee,#b8b8b8)" role="img" aria-label="Photo of business people in an office"></div>
  <div class="abs photo-circle" style="left:517px;top:55px;width:236px;height:236px;background:radial-gradient(circle at 40% 45%,#ddd,#8a8f96)" role="img" aria-label="Photo of a hand dialing a desk telephone"></div>
  <div class="abs photo-circle" style="left:756px;top:94px;width:184px;height:184px;background:radial-gradient(circle at 55% 45%,#f3e4d8,#c7aa92)" role="img" aria-label="Photo of a woman sketching a network diagram"></div>
</section>

<h2 class="abs welcome-title">Welcome to <span>MarbleQuay</span></h2>
<p class="abs welcome-lead">MarbleQuay provides full 24 x 7 Internet Access help desk / technical support services for the hospitality industry.</p>
<h3 class="abs features-title">Services features include:</h3>
<ul class="abs features">
  <li>24 x &nbsp;365 live, immediate, telephone &nbsp;immediate, telephone technical support technical support</li>
  <li>All support personnel are &nbsp;immediate, telephone technical support university or college graduates</li>
  <li>All support &nbsp;immediate, telephone technical support personnel are located in USA or Canada</li>
  <li>Toll free 800 / 888 telephone &nbsp;immediate, telephone technical support number access</li>
  <li>Other specialized IT support available</li>
</ul>
<div class="abs video">
  <div class="video-frame" role="img" aria-label="Testimonial video still of a customer on the phone"><span class="play"></span></div>
  <div class="video-cap"><i></i><i></i>&nbsp;Watch Latest Testimonial Video</div>
</div>

<section class="abs cards">
  <article class="card">
    <div class="card-photo" style="background:linear-gradient(#e4e4e4,#6c7898)" role="img" aria-label="Photo of office phones and a PBX unit"></div>
    <h3><span>Business</span> IP PBX</h3>
    <p>Quis cum nibh tellus, dapibus est duis felis id proin molestie, duis tortor amet quam amet nec...</p>
    <div class="view">View More <span class="plus">+</span></div>
  </article>
  <article class="card">
    <div class="card-photo" style="background:linear-gradient(135deg,#0f2d6a,#6b84b8 55%,#1a2340)" role="img" aria-label="Photo of network cables in a switch"></div>
    <h3><span>Wired IT</span> Networks</h3>
    <p>Quis cum nibh tellus, dapibus est duis felis id proin molestie, duis tortor amet quam amet nec...</p>
    <div class="view">View More <span class="plus">+</span></div>
  </article>
  <article class="card">
    <div class="card-photo" style="background:linear-gradient(#8a8f96,#4a4d52)" role="img" aria-label="Photo of a woman using a laptop on a sofa"></div>
    <h3><span>Wireless IT</span> Networks</h3>
    <p>Quis cum nibh tellus, dapibus est duis felis id proin molestie, duis tortor amet quam amet nec...</p>
    <div class="view">View More <span class="plus">+</span></div>
  </article>
  <article class="card">
    <div class="card-photo" style="background:radial-gradient(circle at 60% 50%,#d9a530,#3a3010 45%,#111)" role="img" aria-label="Photo of glowing fiber optic strands"></div>
    <h3><span>Fiber optic</span> Networks</h3>
    <p>Quis cum nibh tellus, dapibus est duis felis id proin molestie, duis tortor amet quam amet nec...</p>
    <div class="view">View More <span class="plus">+</span></div>
  </article>
</section>

<footer class="abs footer">
  <div class="abs foot-brand"><span class="brand-dot"></span><span class="brand-name">MarbleQuay</span></div>
  <div class="abs vrule" style="left:372px"></div>
  <div class="abs foot-links">Home &nbsp;~&nbsp; Telephone VoIP &nbsp;~&nbsp; IP, LAN &amp; Internet ~&nbsp; Services</div>
  <div class="abs social"><i></i><i></i><i></i><i></i></div>
  <div class="abs copy">Copyright © MarbleQuay A Leading Edge Technology Company</div>
  <div class="abs vrule" style="left:720px"></div>
  <div class="abs foot-contact">
    <h4>Contact Info</h4>
    <div class="fname">MarbleQuay</div>
    <div class="addr">12 Harbour Lane,<br>Eastport Vic 3999</div>
  </div>
  <div class="abs foot-phone">
    <span class="ring"><svg width="16" height="16" viewBox="0 0 24 24"><path fill="#ccc" d="M6.6 10.8a15 15 0 0 0 6.6 6.6l2.2-2.2a1 1 0 0 1 1-.25 11.4 11.4 0 0 0 3.6.57 1 1 0 0 1 1 1V20a1 1 0 0 1-1 1A17 17 0 0 1 3 4a1 1 0 0 1 1-1h3.5a1 1 0 0 1 1 1c0 1.25.2 2.45.57 3.57a1 1 0 0 1-.25 1z"/></svg></span>
    03 5550 1234
  </div>
</footer>
</body>
</html>
```